life insurance quote website design for lavoiesereine.ca

the web site lavoiesereine.ca need a design. we dont like the actuel one but we are open at all new suggestion. visit us at lavoiesereine.ca and you will understand. the principal concurant is devisrapidecouvert.ca, tarifoulot.ca, coutprotegebien.ca. We are a life insurance quote site. we found best price available in the canadien industrie. We absolutly want a design with our form in the front page on the top right side like our concurance, we use wordpress at this time. we want to be able to switch language. and to have a logic form. we want to be able to change the color for each type of insurance quote page.we also need a blog in it to post news. and the site will be SEO accurate.

Target Market(s)

Get client fill the quote form

Industry/Entity Type

Insurance

Number of Pages Required

3 page

Font styles to use
Sans Serif

Requirements
Must have
• logic form on the top right first page
• page template for product info stuff, contact, and who we are, blog
• French site
• custum color
Nice to have
• Wordpress design will be appréciate
• switch language english/french

```html
<!DOCTYPE html>
<html lang="en">
<head>
<meta charset="utf-8">
<title>La Voie Sereine — Life Insurance Quotes</title>
<link href="https://fonts.googleapis.com/css2?family=Open+Sans:wght@400;600;700&family=Roboto+Condensed:wght@400;700&display=swap" rel="stylesheet">
<style>
:root{
  --navy:#1c3d86;
  --navy-dark:#142d66;
  --blue:#2a5cb8;
  --link:#2a5cb8;
  --red:#d62b2b;
  --green:#3aa757;
  --ink:#333;
  --muted:#7a7a7a;
  --line:#dcdcdc;
  --paper:#ffffff;
  --soft:#f1f2f4;
}
*{box-sizing:border-box;margin:0;padding:0}
html,body{width:1200px;height:3156px;overflow:hidden}
body{position:relative;background:var(--paper);font-family:"Open Sans",Arial,sans-serif;color:var(--ink);font-size:14px;line-height:1.55}
.abs{position:absolute}
h2,h3{font-family:"Roboto Condensed","Arial Narrow",sans-serif;font-weight:700;text-transform:uppercase;color:#222}

/* hero */
.hero{left:0;top:0;width:1200px;height:850px}
.hero-photo{position:absolute;inset:0;background:linear-gradient(180deg,#7fb3e4 0%,#a9cdee 38%,#cfdfe9 55%,#8fb06a 72%,#5f8a43 100%)}
.hero-shade{position:absolute;left:0;right:0;bottom:0;height:290px;background:linear-gradient(180deg,rgba(20,45,102,0) 0%,rgba(20,45,102,.85) 100%)}
.brand{left:40px;top:36px;display:flex;align-items:center;gap:12px;font-weight:700;font-size:26px;color:#fff}
.brand-mark{width:30px;height:30px;background:var(--red)}
.topcontact{left:790px;top:22px;font-size:13px;color:#fff;line-height:1.4}
.topcontact .phone{color:var(--red);font-weight:700;font-size:20px}
.social{left:1040px;top:26px;display:flex;gap:8px}
.social span{width:26px;height:26px;border-radius:50%;background:var(--blue)}
.nav{left:680px;top:92px;display:flex;align-items:center;gap:6px;font-size:13px;font-weight:600;text-transform:uppercase;color:#fff}
.nav a{padding:8px 14px;color:#fff;text-decoration:none}
.nav a.active{background:var(--red)}
.lang{border:1px solid rgba(255,255,255,.7);padding:5px 12px;font-size:12px;margin-left:6px}
.arrow{top:390px;width:44px;height:44px;background:rgba(0,0,0,.35);display:flex;align-items:center;justify-content:center}
.welcome{left:100px;top:575px;width:640px;color:#fff}
.welcome h1{font-size:40px;font-weight:700;line-height:1.1;margin-bottom:14px}
.welcome p{font-size:13px;line-height:1.6;opacity:.95}
.dots{left:100px;top:790px;display:flex;gap:8px}
.dots span{width:11px;height:11px;border-radius:50%;background:rgba(255,255,255,.5)}
.dots span:first-child{background:#fff}

/* quote form */
.quote{left:815px;top:190px;width:360px;height:640px;background:#fff;box-shadow:0 4px 18px rgba(0,0,0,.25)}
.quote-head{background:var(--blue);color:#fff;text-align:center;font-size:22px;font-weight:600;padding:10px 0}
.quote-body{padding:14px 22px;font-size:12px}
.q-label{color:var(--blue);font-weight:700;font-size:17px;border-bottom:2px solid var(--blue);padding-bottom:2px;margin:6px 0 8px}
.q-small{color:var(--muted);font-size:11px;margin:6px 0 4px}
.field{height:30px;border:1px solid var(--line);border-radius:2px;font-size:11px;color:#999;padding:6px 8px;display:flex;justify-content:space-between}
.row{display:flex;gap:8px;margin-bottom:8px}
.row .field{flex:1}
.radio{display:flex;gap:14px;font-size:11px;color:#555;margin-bottom:4px}
.radio i{display:inline-block;width:10px;height:10px;border:1px solid #999;border-radius:50%;margin-right:4px;vertical-align:-1px}
.captcha{display:flex;gap:10px;align-items:center;margin-top:12px}
.captcha-code{font-weight:700;letter-spacing:3px;font-size:15px;color:#333;background:var(--soft);padding:4px 10px}
.btn-blue{display:block;margin:16px auto 0;width:130px;background:var(--navy);color:#fff;text-align:center;font-weight:700;font-size:13px;padding:8px 0;text-transform:uppercase}

/* submission */
.sub-photo{left:100px;top:920px;width:430px;height:355px;border:8px solid #fff;box-shadow:0 2px 10px rgba(0,0,0,.2);background:linear-gradient(135deg,#d9c7b2 0%,#a98f74 45%,#6d5a49 100%)}
.submission{left:580px;top:940px;width:520px}
.submission h2{font-size:30px;margin-bottom:4px}
.submission h4{font-size:15px;font-weight:700;margin-bottom:10px}
.submission p{font-size:12.5px;color:#555;margin-bottom:10px}
.ticks{list-style:none;font-size:12.5px;color:#444}
.ticks li{display:flex;align-items:center;gap:8px;margin-bottom:4px}

/* why */
.why{left:0;top:1320px;width:1200px;height:390px;background:linear-gradient(180deg,var(--navy) 0%,var(--navy-dark) 100%)}
.why h2{position:absolute;top:48px;width:100%;text-align:center;color:#fff;font-size:32px}
.why-item{position:absolute;top:130px;width:240px;text-align:center;color:#fff}
.why-item h3{color:#fff;font-size:16px;margin:16px 0 8px}
.why-item p{font-size:12px;opacity:.85;line-height:1.5}

/* blog */
.blog-title{left:100px;top:1775px;font-size:30px}
.blog-main-photo{left:100px;top:1830px;width:470px;height:275px;background:linear-gradient(135deg,#c7b08f 0%,#8c7a62 50%,#4c5e6e 100%)}
.blog-main{left:100px;top:2120px;width:470px}
.post-title{color:var(--link);font-weight:600;font-size:16px;line-height:1.3}
.post-meta{color:var(--red);font-size:12px;margin:6px 0}
.post-text{font-size:12px;color:#666}
.more{font-size:12px;font-weight:700;text-transform:uppercase;color:#333;margin-top:12px}
.post{left:600px;width:500px;display:flex;gap:20px}
.post-thumb{width:130px;height:110px;flex:none}

/* office & insurers */
.office-title{left:100px;top:2470px;font-size:28px}
.office-photo{left:100px;top:2520px;width:165px;height:270px;background:linear-gradient(180deg,#cfe0f0 0%,#9db7cf 50%,#6f8aa3 100%)}
.office-text{left:290px;top:2525px;width:260px;font-size:12px;color:#555}
.office-text p{margin-bottom:10px}
.btn-green{display:inline-block;background:var(--green);color:#fff;font-weight:700;font-size:12px;padding:7px 18px;text-transform:uppercase}
.ins-title{left:670px;top:2470px;font-size:28px}
.ins-grid{left:670px;top:2530px;width:430px;display:grid;grid-template-columns:repeat(3,1fr);gap:22px 20px}
.ins-grid span{height:70px;border-bottom:1px solid var(--line);display:flex;align-items:center;justify-content:center}
.ins-grid span::before{content:"";width:90px;height:26px;background:#cfd2d6;border-radius:3px}

/* footer */
.footer{left:0;top:2840px;width:1200px;height:260px;background:var(--soft)}
.fcol{position:absolute;top:30px;font-size:12px;color:#555}
.fcol h5{font-size:13px;font-weight:700;text-transform:uppercase;color:#222;margin-bottom:12px}
.news-form{display:flex;margin-top:14px}
.news-form .field{width:170px;background:#fff}
.news-form b{background:var(--navy);color:#fff;font-size:11px;padding:7px 12px}
.badge{width:150px;height:58px;background:#d3d6db;border-radius:4px;margin-bottom:18px}
.bottom{left:0;top:3100px;width:1200px;height:56px;background:var(--navy);color:#fff;font-size:12px;text-align:center;line-height:56px}
</style>
</head>
<body>

<section class="abs hero">
  <div class="hero-photo" role="img" aria-label="Photo of a smiling family walking together in a green field under a blue sky"></div>
  <div class="hero-shade"></div>
  <div class="abs brand"><span class="brand-mark"></span>La Voie Sereine</div>
  <div class="abs topcontact">contact@lavoiesereine.ca<br><span class="phone">1-855-000-4217</span></div>
  <div class="abs social"><span></span><span></span><span></span><span></span></div>
  <nav class="abs nav">
    <a class="active">Home</a><a>Who we are</a><a>Contact us</a><a>Blog</a>
    <span class="lang">Français ▾</span>
  </nav>
  <div class="abs arrow" style="left:10px"><svg width="14" height="20"><path d="M11 2 3 10l8 8" stroke="#fff" stroke-width="3" fill="none"/></svg></div>
  <div class="abs arrow" style="left:1146px;top:390px;opacity:0"></div>
  <div class="abs welcome">
    <h1>Welcome To &nbsp;La Voie Sereine</h1>
    <p>We compare life insurance prices across leading Canadian insurers so you find the best coverage at the lowest cost. Fill in the short quote form, answer a few questions and receive a free, no obligation quote within minutes from our trusted licensed advisors.</p>
  </div>
  <div class="abs dots"><span></span><span></span><span></span></div>

  <form class="abs quote">
    <div class="quote-head">Quote Request</div>
    <div class="quote-body">
      <div class="q-label">Product</div>
      <div class="q-small">Type of insurance</div>
      <div class="field">Select<span>▾</span></div>
      <div class="q-label" style="margin-top:14px">Applicant</div>
      <div class="row"><div class="field">First name</div><div class="field">Last name</div></div>
      <div class="row"><div class="field">Email</div><div class="field">Phone</div></div>
      <div class="q-small">Date of birth</div>
      <div class="row"><div class="field">Day<span>▾</span></div><div class="field">Month<span>▾</span></div><div class="field">Year<span>▾</span></div></div>
      <div class="q-small">Gender</div>
      <div class="radio"><span><i></i>Male</span><span><i></i>Female</span></div>
      <div class="q-small">Smoker</div>
      <div class="radio"><span><i></i>Yes</span><span><i></i>No</span></div>
      <div class="radio"><span><i></i>I accept the terms and privacy policy</span></div>
      <div class="captcha"><span class="q-small" style="margin:0">Captcha</span><span class="captcha-code">R8KVE</span><div class="field" style="flex:1">Code</div></div>
      <span class="btn-blue">Continue</span>
    </div>
  </form>
</section>

<div class="abs sub-photo" role="img" aria-label="Photo of a couple reviewing insurance documents on a laptop"></div>
<section class="abs submission">
  <h2>Online Life Insurance Submission</h2>
  <h4>Find The Best Insurance At The Best Price</h4>
  <p>Whether you are looking for term, whole or critical illness coverage, our free online service compares offers from major Canadian insurers. Tell us about your needs and we match you with the plan that protects your family at a fair price, with no pressure and no hidden fees.</p>
  <ul class="ticks">
    <li><svg width="14" height="14"><circle cx="7" cy="7" r="7" fill="#d62b2b"/><path d="M3.5 7l2.5 2.5 4.5-5" stroke="#fff" stroke-width="1.8" fill="none"/></svg>Permanent life insurance – whole life coverage</li>
    <li><svg width="14" height="14"><circle cx="7" cy="7" r="7" fill="#d62b2b"/><path d="M3.5 7l2.5 2.5 4.5-5" stroke="#fff" stroke-width="1.8" fill="none"/></svg>Disability insurance – income protection</li>
    <li><svg width="14" height="14"><circle cx="7" cy="7" r="7" fill="#d62b2b"/><path d="M3.5 7l2.5 2.5 4.5-5" stroke="#fff" stroke-width="1.8" fill="none"/></svg>Mortgage insurance – home loans</li>
    <li><svg width="14" height="14"><circle cx="7" cy="7" r="7" fill="#d62b2b"/><path d="M3.5 7l2.5 2.5 4.5-5" stroke="#fff" stroke-width="1.8" fill="none"/></svg>Critical illness insurance</li>
  </ul>
</section>

<section class="abs why">
  <h2>Why Choose Us</h2>
  <div class="why-item" style="left:90px">
    <svg width="84" height="96" viewBox="0 0 84 96"><path d="M42 2 80 14v30c0 26-18 42-38 50C22 86 4 70 4 44V14Z" fill="#d62b2b" stroke="#fff" stroke-width="3"/><path d="M42 66 26 50a9 9 0 0 1 16-11 9 9 0 0 1 16 11Z" fill="#fff"/></svg>
    <h3>Life Insurance</h3><p>Simple term or permanent plans that keep your loved ones safe for years to come.</p>
  </div>
  <div class="why-item" style="left:350px">
    <svg width="84" height="96" viewBox="0 0 84 96"><path d="M42 2 80 14v30c0 26-18 42-38 50C22 86 4 70 4 44V14Z" fill="#d62b2b" stroke="#fff" stroke-width="3"/><text x="42" y="62" text-anchor="middle" font-family="Open Sans,sans-serif" font-weight="700" font-size="34" fill="#fff">$</text></svg>
    <h3>Salary Insurance</h3><p>Protect your income if illness or injury keeps you away from work for a while.</p>
  </div>
  <div class="why-item" style="left:610px">
    <svg width="84" height="96" viewBox="0 0 84 96"><path d="M42 2 80 14v30c0 26-18 42-38 50C22 86 4 70 4 44V14Z" fill="#d62b2b" stroke="#fff" stroke-width="3"/><path d="M24 48 42 32l18 16h-5v16H29V48Z" fill="#fff"/></svg>
    <h3>Mortgage Insurance</h3><p>Make sure your home stays with your family whatever happens along the way.</p>
  </div>
  <div class="why-item" style="left:870px">
    <svg width="84" height="96" viewBox="0 0 84 96"><path d="M42 2 80 14v30c0 26-18 42-38 50C22 86 4 70 4 44V14Z" fill="#d62b2b" stroke="#fff" stroke-width="3"/><path d="M36 30h12v12h12v12H48v12H36V54H24V42h12Z" fill="#fff"/></svg>
    <h3>Critical Illness Insurance</h3><p>A tax free lump sum to help you focus on recovery when it matters most.</p>
  </div>
</section>

<h2 class="abs blog-title">From Our Blog</h2>
<div class="abs blog-main-photo" role="img" aria-label="Photo of hands pointing at a tablet with financial charts"></div>
<article class="abs blog-main">
  <div class="post-title">Nemo enim ipsam voluptatem quia voluptas sit</div>
  <div class="post-meta">April 23 2016 &nbsp;|&nbsp; 2 comments &nbsp;|&nbsp; 3 hours ago</div>
  <p class="post-text">Sed ut perspiciatis unde omnis iste natus error sit voluptatem accusantium doloremque laudantium, totam rem aperiam, eaque ipsa quae ab illo inventore veritatis et quasi architecto.</p>
  <div class="more">Read more ›</div>
</article>
<article class="abs post" style="top:1800px">
  <div class="post-thumb" role="img" aria-label="Photo of an advisor meeting a client" style="background:linear-gradient(135deg,#b9c7d6,#5d7389)"></div>
  <div><div class="post-title">How to proceed?</div><p class="post-text" style="margin-top:8px">Simply fill in the quote form, choose your product and an advisor will contact you with the best available rates from our partner insurers.</p></div>
</article>
<article class="abs post" style="top:1990px">
  <div class="post-thumb" role="img" aria-label="Photo of a financial advisor at a desk" style="background:linear-gradient(135deg,#d8cbb8,#7b6b58)"></div>
  <div><div class="post-title">Competent financial advisors Security</div><p class="post-text" style="margin-top:8px">Our licensed advisors are trained to explain every option clearly so you choose coverage with confidence and total peace of mind.</p></div>
</article>
<article class="abs post" style="top:2180px">
  <div class="post-thumb" role="img" aria-label="Photo of a person calculating expenses" style="background:linear-gradient(135deg,#c6d3c0,#6a7f63)"></div>
  <div><div class="post-title">The importance of not overpaying</div><p class="post-text" style="margin-top:8px">Comparing several quotes can save hundreds each year. Learn why the lowest price and the right coverage can go hand in hand.</p></div>
</article>

<h2 class="abs office-title">Our Office</h2>
<div class="abs office-photo" role="img" aria-label="Photo of a modern glass office tower"></div>
<div class="abs office-text">
  <p>Our team works from a bright downtown office where advisors welcome clients by appointment every weekday.</p>
  <p>Drop by to meet us in person, or reach us by phone and email for a fast answer to all your questions.</p>
  <p>We serve families across the province in French and English.</p>
  <span class="btn-green">Read more</span>
</div>
<h2 class="abs ins-title">Insurance Compagnie</h2>
<div class="abs ins-grid"><span></span><span></span><span></span><span></span><span></span><span></span></div>

<footer class="abs footer">
  <div class="fcol" style="left:100px;width:280px">
    <h5>Sign up for Newsletter</h5>
    <p>Receive our latest articles, tips and exclusive offers directly in your inbox.</p>
    <div class="news-form"><div class="field">Enter email</div><b>SUBSCRIBE</b></div>
  </div>
  <div class="fcol" style="left:430px;width:240px">
    <h5>Hours of Operation</h5>
    <p>Monday to Friday: 9am to 5pm<br>Saturday: 10am to 2pm</p>
    <p style="margin-top:8px">Toll free: 1-855-000-4217<br>contact@lavoiesereine.ca</p>
    <div style="display:flex;gap:8px;margin-top:10px"><span style="width:22px;height:22px;border-radius:50%;background:var(--blue)"></span><span style="width:22px;height:22px;border-radius:50%;background:var(--blue)"></span><span style="width:22px;height:22px;border-radius:50%;background:var(--blue)"></span></div>
  </div>
  <div class="fcol" style="left:720px;width:150px">
    <h5>Our Offices</h5>
    <p>Montréal<br>Québec<br>Laval<br>Longueuil<br>Gatineau<br>Sherbrooke<br>Trois-Rivières</p>
  </div>
  <div class="fcol" style="left:930px">
    <div class="badge" role="img" aria-label="Financial services regulator membership badge"></div>
    <div class="badge" role="img" aria-label="Security certificate badge"></div>
  </div>
</footer>
<div class="abs bottom">©2015 – 2016 – La Voie Sereine. All Rights Reserved.</div>

</body>
</html>
```